FERNLOOP Guiding Answers Across The Digital Frontier\Government Contracting IT, Software, Networks

We need a business card design for a new Government Joint Venture based out of Omaha, NE. We provide all types of technology needs to all types of Government agencies. I have attached logo and capability statement to identify our companies industry and offerings. extremely import information that needs to be identified on the cards is SBA: 8(a), SBA: SDB, SBA: HUBZone

Target Market(s)

Government Contracting Officers

Industry/Entity Type

Business

Contact Information for Business Card

Delia Frost
Vice President
7281 W 48th Avenue
Omaha, NE 68342
P: 402-555-3172
F: 402-555-3173
Toll: 855-555-2046
delia@fernloop.co
http://www.fernloop.co
Gideon Vally
President
7281 W 48th Avenue
Omaha, NE 68342
P: 402-555-3172
F: 402-555-3173
Toll: 855-555-2046
gideon@fernloop.co
http://www.fernloop.co

Number of Pages Required

4 page

Font styles to use
Serif

Requirements
Must have
• Look and feel should be technical.

```html
<!DOCTYPE html>
<html lang="en">
<head>
<meta charset="utf-8">
<title>FERNLOOP Business Card</title>
<link href="https://fonts.googleapis.com/css2?family=Saira+Semi+Condensed:wght@400;500;700&display=swap" rel="stylesheet">
<style>
  :root {
    --violet: #3b22d4;
    --violet-deep: #2510a0;
    --violet-text: #3a2bc4;
    --ink: #1a1a1a;
    --paper: #ffffff;
    --paper-tone: #ececec;
    --ground: #d9d6d2;
    --rule-gray: #b9b9b9;
  }
  html, body {
    margin: 0;
    width: 1200px;
    height: 871px;
    overflow: hidden;
    background: var(--ground);
    font-family: "Saira Semi Condensed", Arial, sans-serif;
  }
  .canvas {
    position: relative;
    width: 1200px;
    height: 871px;
  }
  .card {
    position: absolute;
    width: 540px;
    height: 309px;
    top: 281px;
    overflow: hidden;
    box-shadow: 0 8px 22px rgba(0,0,0,0.25);
  }
  /* Back side */
  .card-back {
    left: 40px;
    background: linear-gradient(160deg, var(--violet) 0%, var(--violet-deep) 100%);
    color: var(--paper);
  }
  .back-mark {
    position: absolute;
    left: 0; right: 0; top: 92px;
    display: flex;
    flex-direction: column;
    align-items: center;
    gap: 12px;
  }
  .back-mark .dot {
    width: 56px; height: 56px;
    border-radius: 50%;
    background: var(--paper);
  }
  .back-mark .brand {
    font-size: 30px;
    font-weight: 500;
    letter-spacing: 3px;
    color: var(--paper);
  }
  .back-url {
    position: absolute;
    left: 0; right: 0; top: 222px;
    text-align: center;
    font-size: 14px;
    letter-spacing: 1px;
    color: var(--paper);
  }
  /* Front side */
  .card-front {
    left: 620px;
    background: linear-gradient(135deg, var(--paper-tone) 0%, var(--paper) 55%, var(--paper-tone) 100%);
  }
  .front-surface {
    position: absolute;
    inset: 0;
  }
  .front-logo {
    position: absolute;
    left: 38px; top: 40px;
    width: 200px;
    display: flex;
    flex-direction: column;
    align-items: center;
    gap: 14px;
  }
  .front-logo .dot {
    width: 92px; height: 92px;
    border-radius: 50%;
    background: var(--violet-text);
  }
  .front-logo .brand {
    font-size: 34px;
    font-weight: 500;
    letter-spacing: 2px;
    color: var(--violet-text);
  }
  .contact {
    position: absolute;
    left: 300px; top: 42px;
    color: var(--ink);
  }
  .contact .person {
    margin: 0 0 0 22px;
    font-size: 21px;
    font-weight: 700;
  }
  .contact .role {
    margin: 2px 0 14px 22px;
    font-size: 15px;
    font-weight: 500;
    color: var(--violet-text);
  }
  .contact .address {
    margin: 0 0 8px 0;
    font-size: 13px;
  }
  .contact ul {
    list-style: none;
    margin: 0; padding: 0;
    font-size: 14px;
  }
  .contact li {
    display: flex;
    align-items: center;
    gap: 10px;
    height: 22px;
  }
  .contact li svg { flex: none; }
  .contact .note { margin-left: 10px; }
  .sba-line {
    position: absolute;
    left: 22px; top: 258px;
    font-size: 14px;
    font-style: italic;
    color: var(--paper);
    letter-spacing: 0.5px;
  }
</style>
</head>
<body>
<div class="canvas">

  <section class="card card-back" aria-label="Card back">
    <div class="back-mark">
      <span class="dot"></span>
      <span class="brand">FERNLOOP</span>
    </div>
    <p class="back-url">www.fernloop.com</p>
  </section>

  <section class="card card-front" aria-label="Card front">
    <svg class="front-surface" width="540" height="309" viewBox="0 0 540 309">
      <path d="M250 262 L540 262 L540 272 L262 272 Z" fill="var(--rule-gray)"/>
      <path d="M0 248 L226 248 C246 248 246 272 268 272 L540 272 L540 309 L0 309 Z" fill="var(--violet)"/>
    </svg>

    <div class="front-logo">
      <span class="dot"></span>
      <span class="brand">FERNLOOP</span>
    </div>

    <div class="contact">
      <p class="person">Delia Frost</p>
      <p class="role">Vice President</p>
      <p class="address">7281 W 48th Avenue Omaha, NE 68342</p>
      <ul>
        <li>
          <svg width="14" height="12" viewBox="0 0 14 12"><path d="M1 4 Q7 -1 13 4 L11 6 L9 4 L5 4 L3 6 Z" fill="var(--violet-text)"/><rect x="3" y="7" width="8" height="4" rx="1" fill="var(--violet-text)"/></svg>
          <span>402-555-3172</span>
        </li>
        <li>
          <svg width="14" height="12" viewBox="0 0 14 12"><rect x="1" y="2" width="12" height="9" rx="1" fill="none" stroke="var(--violet-text)" stroke-width="1.6"/><rect x="4" y="4" width="6" height="3" fill="var(--violet-text)"/></svg>
          <span>402-555-3173</span>
        </li>
        <li>
          <svg width="14" height="12" viewBox="0 0 14 12"><path d="M1 4 Q7 -1 13 4 L11 6 L9 4 L5 4 L3 6 Z" fill="var(--violet-text)"/><rect x="3" y="7" width="8" height="4" rx="1" fill="var(--violet-text)"/></svg>
          <span>855-555-2046<span class="note">Toll Free</span></span>
        </li>
        <li>
          <svg width="14" height="12" viewBox="0 0 14 12"><rect x="1" y="2" width="12" height="9" fill="var(--violet-text)"/><path d="M1 2 L7 7 L13 2" fill="none" stroke="var(--paper)" stroke-width="1.2"/></svg>
          <span>delia@fernloop.co</span>
        </li>
      </ul>
    </div>

    <p class="sba-line">SBA: 8(a), SBA: SDB, SBA: HUBZone</p>
  </section>

</div>
</body>
</html>
```